Lumora Education - new College Consulting company in San Francisco needs a flyer design

We need a logo design for a new college admissions consulting business in San Francisco Bay Area and San Jose called 'Lumora Education'. We plan to develop tailor-made strategies for each students dreams and aspirations and will help provide them with online classes and in-person consulting starting Summer 2022.
Lumora Education plans on providing a free first time consulting to attract clients and grow our client base from there.
Lumora Education has a small team of consultants who have degrees from Economics/Business, Biology, and Computer Science who can provide tailored guidance to meet student and parent expectations and spend the time to walk them throughout the process.
Please refer to attached logos for the company and to create a flyer.
Target Market(s)
Competitive College Consulting
Industry/Entity Type
Education Consulting
Look and feel

```html
<!DOCTYPE html>
<html lang="en">
<head>
<meta charset="utf-8">
<title>Lumora Education Flyer</title>
<link rel="stylesheet" href="https://fonts.googleapis.com/css2?family=Roboto:wght@400;500;700&display=swap">
<style>
  :root {
    --coral: #f9938a;
    --coral-deep: #eb837a;
    --ink: #1f1f1f;
    --text: #2b2b2b;
    --footer: #2a2a2b;
    --white: #ffffff;
    --photo-warm: #b48a6a;
    --photo-shade: #4a3d36;
  }
  * { box-sizing: border-box; margin: 0; padding: 0; }
  html, body { width: 848px; height: 1200px; overflow: hidden; background: var(--white); }
  body { font-family: "Roboto", Arial, sans-serif; color: var(--text); }
  .flyer { position: relative; width: 848px; height: 1200px; overflow: hidden; background: var(--white); }
  .backdrop { position: absolute; inset: 0; }

  .brand {
    position: absolute; left: 20px; top: 16px; text-align: right; width: 144px;
  }
  .brand-row { display: flex; align-items: center; justify-content: flex-end; gap: 6px; }
  .brand-name { font-size: 13px; font-weight: 500; color: var(--ink); }
  .brand-mark { width: 10px; height: 10px; border-radius: 50%; background: var(--ink); }
  .brand-tagline { font-size: 10.5px; color: var(--ink); margin-top: 3px; }

  .title { position: absolute; left: 53px; top: 622px; font-weight: 700; line-height: 1; }
  .title-top { display: block; font-size: 62px; color: var(--ink); letter-spacing: -1px; }
  .title-bottom { display: block; font-size: 76px; color: var(--coral); letter-spacing: -1px; margin-top: 2px; }

  .section-heading { font-size: 29px; font-weight: 700; color: var(--ink); line-height: 1; }
  .rule { width: 72px; height: 3px; background: var(--coral); margin-top: 16px; }

  .about { position: absolute; left: 56px; top: 810px; width: 346px; }
  .about-text {
    margin-top: 23px; font-size: 15px; line-height: 25.1px; text-align: justify; color: var(--text);
  }

  .courses { position: absolute; left: 462px; top: 689px; width: 340px; }
  .course-list { list-style: none; margin-top: 38px; }
  .course { position: relative; height: 101px; padding-left: 72px; }
  .course-icon {
    position: absolute; left: 0; top: 0; width: 55px; height: 55px; background: var(--coral);
    display: flex; align-items: center; justify-content: center;
  }
  .course-icon.dark { background: var(--ink); }
  .course-name { font-size: 22px; font-weight: 500; color: var(--ink); line-height: 1; padding-top: 1px; }
  .course-desc { font-size: 15.5px; line-height: 20px; margin-top: 11px; color: var(--text); }

  .contact {
    position: absolute; top: 1150px; display: flex; align-items: center; gap: 11px;
    color: var(--white); font-size: 17px;
  }
  .contact-phone { left: 43px; }
  .contact-web { right: 43px; }
  .contact-icon {
    width: 34px; height: 34px; background: var(--coral);
    display: flex; align-items: center; justify-content: center;
  }
</style>
</head>
<body>
<div class="flyer">
  <svg class="backdrop" width="848" height="1200" viewBox="0 0 848 1200">
    <defs>
      <linearGradient id="campus-tones" x1="0" y1="0" x2="1" y2="1">
        <stop offset="0" stop-color="#8f7b66"/>
        <stop offset="0.45" stop-color="var(--photo-warm)"/>
        <stop offset="1" stop-color="var(--photo-shade)"/>
      </linearGradient>
      <clipPath id="hero-clip">
        <path d="M0,0 H848 V334 C740,500 600,562 440,562 C260,562 100,470 0,350 Z"/>
      </clipPath>
    </defs>
    <path d="M0,330 H848 V630 C830,560 790,530 730,535 C640,545 560,603 430,603 C250,603 90,520 0,428 Z" fill="var(--coral)"/>
    <path d="M712,490 C760,440 820,450 848,520 V600 C830,520 780,480 712,490 Z" fill="var(--coral-deep)"/>
    <path d="M740,510 C780,480 830,495 848,560 V610 C830,550 790,515 740,510 Z" fill="var(--coral-deep)" opacity="0.7"/>
    <g clip-path="url(#hero-clip)">
      <rect x="0" y="0" width="848" height="600" fill="url(#campus-tones)" role="img" aria-label="Photo of smiling students with backpacks and books in front of a university building"/>
    </g>
    <ellipse cx="118" cy="14" rx="138" ry="70" fill="var(--white)"/>
    <path d="M0,1095 Q424,1220 848,1095 V1200 H0 Z" fill="var(--footer)"/>
  </svg>

  <header class="brand">
    <div class="brand-row"><span class="brand-name">Lumora Education</span><span class="brand-mark"></span></div>
    <div class="brand-tagline">Learning is a phenomenom</div>
  </header>

  <h1 class="title"><span class="title-top">Lumora</span><span class="title-bottom">Education</span></h1>

  <section class="about">
    <h2 class="section-heading">About Consulting</h2>
    <div class="rule"></div>
    <p class="about-text">Lorem ipsum dolor aliquip ex sit amet, consectetur adipiscing elit, sed it do eiusmod tempor incididunt ut labore et dolore magna aliqua. Ut enim ad minim veniam, quis dolor nostrud exercitation ullamco laboris nisi ut aliquip ex ea commodo consequat. Duis auterer irure dolor in reprehenderit in voluptate velit esse cillum dolore eu fugiat nulla pariatur.</p>
  </section>

  <section class="courses">
    <h2 class="section-heading">Our Courses:</h2>
    <div class="rule"></div>
    <ul class="course-list">
      <li class="course">
        <span class="course-icon">
          <svg width="30" height="30" viewBox="0 0 30 30" fill="none" stroke="#fff" stroke-width="1.6">
            <path d="M4,27 H26"/><rect x="6" y="18" width="4" height="9"/><rect x="13" y="14" width="4" height="13"/><rect x="20" y="17" width="4" height="10"/>
            <path d="M5,14 L12,8 L16,11 L24,4"/><path d="M20,4 H24 V8"/>
          </svg>
        </span>
        <h3 class="course-name">Economics/Business</h3>
        <p class="course-desc">Nemo enim ipsam voluptatem quia voluptas sit aspernatur.</p>
      </li>
      <li class="course">
        <span class="course-icon dark">
          <svg width="32" height="32" viewBox="0 0 32 32" fill="none" stroke="#fff" stroke-width="1.6">
            <circle cx="16" cy="16" r="13"/><circle cx="11" cy="12" r="3"/><circle cx="20" cy="20" r="4"/><path d="M14,20 L9,24"/>
          </svg>
        </span>
        <h3 class="course-name">Biology</h3>
        <p class="course-desc">Nemo enim ipsam voluptatem quia voluptas sit aspernatur.</p>
      </li>
      <li class="course">
        <span class="course-icon">
          <svg width="32" height="32" viewBox="0 0 32 32" fill="none" stroke="#fff" stroke-width="1.6">
            <rect x="4" y="10" width="20" height="14" rx="1"/><path d="M10,28 H18 M14,24 V28"/>
            <path d="M20,10 A4,4 0 0 1 27,8 A3,3 0 0 1 28,14 H22"/>
          </svg>
        </span>
        <h3 class="course-name">Computer Science</h3>
        <p class="course-desc">Nemo enim ipsam voluptatem quia voluptas sit aspernatur.</p>
      </li>
    </ul>
  </section>

  <footer>
    <div class="contact contact-phone">
      <span class="contact-icon">
        <svg width="18" height="18" viewBox="0 0 24 24" fill="#fff"><path d="M6.6 10.8a15.1 15.1 0 0 0 6.6 6.6l2.2-2.2a1 1 0 0 1 1-.25 11.4 11.4 0 0 0 3.6.57 1 1 0 0 1 1 1V20a1 1 0 0 1-1 1A17 17 0 0 1 3 4a1 1 0 0 1 1-1h3.5a1 1 0 0 1 1 1c0 1.25.2 2.45.57 3.57a1 1 0 0 1-.25 1z"/></svg>
      </span>
      <span>(+1) 04 555 0123</span>
    </div>
    <div class="contact contact-web">
      <span>lumoraeducation.com</span>
      <span class="contact-icon">
        <svg width="20" height="16" viewBox="0 0 20 16" fill="none" stroke="#fff" stroke-width="1.6"><rect x="1" y="1" width="18" height="14"/><path d="M1,1 L10,9 L19,1 M1,15 L8,7.5 M19,15 L12,7.5"/></svg>
      </span>
    </div>
  </footer>
</div>
</body>
</html>
```